v eLiquid Label

We are an electronic cigarette eLiquid manufacturer with an outdated label design which needs to be updated and become more modern. All information listed on the label cannot be changed or removed.

There are 4 colour coding on the labels that cannot change.
0mg is white
12mg is yellow
18mg is blue
24mg is red

We prefer a blue type background however are not committed to it with the proper design however if a new colour is chosen it must compliment the colour band for each colour coding

The "dots" on the front of the bottle need to be larger.

The "V" on the front needs to be in this font however we can accept slight changes to it for effect.

Issues we are facing:
The 0mg and the 18mg look too close in colour and need to be completely different in colouring.

The background colouring is too dark and you cannot see the 50/50 in the watermark.

Reason: We have not received a design which is suitable to our needs. We have see a few close ones however not exact. Thanks

Reason: I was forced to go out of country for a family emergency and to be fair I am extending the deadline

```html
<!DOCTYPE html>
<html lang="en">
<head>
<meta charset="utf-8">
<title>Velora Sweet Tobacco E-Liquid Labels</title>
<link href="https://fonts.googleapis.com/css2?family=PT+Sans+Narrow:wght@400;700&family=Open+Sans:wght@700;800&display=swap" rel="stylesheet">
<style>
  :root{
    --stage-a:#1c2a8f;
    --stage-b:#111735;
    --panel:#2f8fd8;
    --panel-light:#5fb0ea;
    --ink:#0b1c36;
    --paper:#ffffff;
    --zero:#1b7fd0;
    --yellow:#ffe500;
    --yellow-ink:#a89300;
    --navy:#252a6e;
    --red:#e8202a;
    --hazard:#ffd400;
  }
  *{box-sizing:border-box;margin:0;padding:0}
  html,body{width:1200px;height:1000px;overflow:hidden}
  body{
    background:radial-gradient(ellipse at 20% 30%,var(--stage-a) 0%,#1a2260 45%,var(--stage-b) 100%);
    font-family:"PT Sans Narrow",Arial,sans-serif;
    position:relative;
  }
  .label{position:absolute;left:300px;width:600px;height:237px;--code:var(--zero);--code-ink:var(--zero);--strip-bg:var(--paper);--dot:var(--zero);--dot-ink:var(--paper);--ring-ink:var(--zero)}
  .label.mg0{--code:var(--paper);--ring-ink:var(--zero)}
  .label.mg12{--code:var(--yellow);--code-ink:var(--yellow-ink);--strip-bg:var(--yellow);--dot:var(--yellow);--dot-ink:var(--navy);--ring-ink:var(--navy)}
  .label.mg18{--code:var(--navy);--code-ink:var(--navy);--dot:var(--navy);--ring-ink:var(--paper)}
  .label.mg24{--code:var(--red);--code-ink:var(--red);--dot:var(--red);--ring-ink:var(--paper)}

  .strip{
    position:absolute;left:0;width:600px;height:14px;
    background:var(--strip-bg);border:1.5px solid var(--code-ink);
    font-family:"Open Sans",Arial,sans-serif;font-weight:800;font-size:10.5px;
    letter-spacing:1.4px;color:var(--code-ink);line-height:11px;
    white-space:nowrap;overflow:hidden;text-align:center;word-spacing:2px;
    box-shadow:0 3px 6px rgba(0,0,0,.5);
  }
  .mg12 .strip{color:var(--yellow-ink);border-color:var(--yellow)}
  .strip.top{top:0}
  .strip.bottom{top:223px}

  .panel{
    position:absolute;top:18px;left:0;width:600px;height:202px;overflow:hidden;
    background:linear-gradient(100deg,var(--panel) 0%,#3797dd 55%,#4aa2e2 80%,var(--panel) 100%);
    border-top:4px solid var(--code);
    box-shadow:0 4px 10px rgba(0,0,0,.55);
    color:var(--ink);
  }
  .swirl{position:absolute;inset:0;width:600px;height:198px}
  .hazard{position:absolute;left:6px;top:6px;width:26px;height:22px}
  .watermark{
    position:absolute;left:212px;top:-6px;width:190px;
    font-family:"Open Sans",Arial,sans-serif;font-weight:800;font-size:54px;line-height:48px;
    color:var(--panel-light);opacity:.75;letter-spacing:-1px;
  }
  .brand{
    position:absolute;left:220px;top:46px;width:160px;text-align:center;
    font-weight:700;font-size:42px;color:var(--paper);line-height:44px;
  }
  .flavour{
    position:absolute;left:220px;top:100px;width:160px;text-align:center;
    font-weight:700;font-size:21px;color:var(--paper);letter-spacing:.5px;
  }
  .copy-fr{
    position:absolute;left:8px;top:4px;width:194px;text-align:right;
    font-size:10.4px;line-height:13.2px;
  }
  .copy-en{
    position:absolute;left:400px;top:4px;width:188px;
    font-size:10.4px;line-height:13.2px;
  }
  .copy-fr b,.copy-en b{font-weight:700}
  .gap{display:block;height:4px}
  .record{
    position:absolute;left:398px;top:144px;width:200px;height:20px;
    background:var(--paper);font-size:10px;line-height:20px;padding-left:4px;
    display:flex;gap:52px;
  }
  .rule{position:absolute;left:0;top:167px;width:600px;height:4px;background:var(--code)}
  .mg0 .rule{height:3px}
  .badge{position:absolute;left:276px;top:145px;width:48px;height:48px}
  .badge .ring{fill:var(--code)}
  .badge .ring-text{font-family:"Open Sans",Arial,sans-serif;font-weight:700;font-size:5px;letter-spacing:.6px;fill:var(--ring-ink)}
  .badge .dot{fill:var(--dot);stroke:var(--paper);stroke-width:2.5}
  .badge .value{font-family:"Open Sans",Arial,sans-serif;font-weight:800;font-size:15px;fill:var(--dot-ink)}
  .mg0 .badge .value{font-size:10px}
  .foot{position:absolute;top:172px;left:0;width:600px;height:26px;color:var(--paper);font-size:10.4px;line-height:11.5px}
  .foot .fr{position:absolute;left:24px;top:3px;width:178px;text-align:right}
  .foot .size{position:absolute;left:330px;top:3px;width:60px;text-align:center;font-weight:700;font-size:11px}
  .foot .en{position:absolute;left:400px;top:3px;width:196px}
</style>
</head>
<body>

<!-- 0 mg -->
<section class="label mg0" style="top:0">
  <div class="strip top">NICOTINE FREE &nbsp; NICOTINE FREE &nbsp; NICOTINE FREE &nbsp; NICOTINE FREE &nbsp; NICOTINE FREE</div>
  <div class="panel">
    <svg class="swirl" viewBox="0 0 600 198" aria-hidden="true"><path d="M0 40 C120 10 200 90 320 40 S520 20 600 60" fill="none" stroke="rgba(255,255,255,.18)"/><path d="M0 60 C140 30 220 110 340 60 S540 40 600 90" fill="none" stroke="rgba(255,255,255,.12)"/></svg>
    <svg class="hazard" viewBox="0 0 26 22" aria-hidden="true"><path d="M13 1 L25 21 H1 Z" fill="var(--hazard)" stroke="#000" stroke-width="1.2"/><circle cx="13" cy="12" r="3.2" fill="#000"/><path d="M8 17 L18 14 M8 14 L18 17" stroke="#000" stroke-width="1.3"/></svg>
    <div class="watermark">50/50<br>50/50<br>50/50</div>
    <div class="brand">Velora</div>
    <div class="flavour">SWEET TOBACCO</div>
    <div class="copy-fr"><b>CONTENIR NOCIF</b><br>Ne pas avaler.<br>Ne pas mettre dans les yeux ou sur la peau ou les vêtements.<br>Tenir hors de portée des enfants et des animaux.<br><b>INGRÉDIENTS:</b> Propylène Glycol, Glycérine, Alcool de Qualité Alimentaire, Arômes Naturel et Artificiels.<span class="gap"></span><b>En cas d'ingestion consulter centre antipoison ou un médecin immédiatement. Peux contenir de noix.</b></div>
    <div class="copy-en"><b>WARNING CONTENTS HARMFUL</b><br>Do not swallow.<br>Do not get in eyes or on skin or clothing.<br>Keep out of reach of children and pets.<br><b>IN GREDIENTS:</b> Propylene Glycol, Vegetable Glycerin, Food Grade Alcohol, Natural and Artificial Flavours.<span class="gap"></span><b>If swallowed consult poison control centre or a doctor immediately.<br>May contain nuts.</b></div>
    <div class="record"><span>BATCH :</span><span>EXPIRES :</span></div>
    <div class="rule"></div>
    <svg class="badge" viewBox="0 0 48 48" aria-label="Nicotine strength zero">
      <defs><path id="arc-0" d="M7 24 A17 17 0 0 1 41 24"/></defs>
      <circle class="ring" cx="24" cy="24" r="23"/>
      <text class="ring-text"><textPath href="#arc-0" startOffset="50%" text-anchor="middle">NICOTINE LEVEL</textPath></text>
      <circle class="dot" cx="24" cy="26" r="13"/>
      <text class="value" x="24" y="29.5" text-anchor="middle">ZERO</text>
    </svg>
    <div class="foot"><div class="fr">Produit et emballé exclusivement pour:<br>4471920 Northfield Inc, Ashby ON, K0A 1B0</div><div class="size">30 ml<br>E-LIQUID</div><div class="en">Produced and Packaged exclusively for :<br>4471920 Northfield Inc, Ashby ON, K0A 1B0</div></div>
  </div>
  <div class="strip bottom">ZÉRO NICOTINE &nbsp; ZÉRO NICOTINE &nbsp; ZÉRO NICOTINE &nbsp; ZÉRO NICOTINE &nbsp; ZÉRO NICOTINE</div>
</section>

<!-- 12 mg -->
<section class="label mg12" style="top:250px">
  <div class="strip top">12 mg/ml NICOTINE &nbsp; 12 mg/ml NICOTINE &nbsp; 12 mg/ml NICOTINE &nbsp; 12 mg/ml NICOTINE</div>
  <div class="panel">
    <svg class="swirl" viewBox="0 0 600 198" aria-hidden="true"><path d="M0 40 C120 10 200 90 320 40 S520 20 600 60" fill="none" stroke="rgba(255,229,0,.35)"/><path d="M0 60 C140 30 220 110 340 60 S540 40 600 90" fill="none" stroke="rgba(255,255,255,.12)"/></svg>
    <svg class="hazard" viewBox="0 0 26 22" aria-hidden="true"><path d="M13 1 L25 21 H1 Z" fill="var(--hazard)" stroke="#000" stroke-width="1.2"/><circle cx="13" cy="12" r="3.2" fill="#000"/><path d="M8 17 L18 14 M8 14 L18 17" stroke="#000" stroke-width="1.3"/></svg>
    <div class="watermark">50/50<br>50/50<br>50/50</div>
    <div class="brand">Velora</div>
    <div class="flavour">SWEET TOBACCO</div>
    <div class="copy-fr"><b>CONTENIR NOCIF</b><br>Ne pas avaler.<br>Ne pas mettre dans les yeux ou sur la peau ou les vêtements.<br>Tenir hors de portée des enfants et des animaux.<br><b>INGRÉDIENTS:</b> Propylène Glycol, Glycérine, Alcool de Qualité Alimentaire, Arômes Naturel et Artificiels.<span class="gap"></span><b>En cas d'ingestion consulter centre antipoison ou un médecin immédiatement. Peux contenir de noix.</b></div>
    <div class="copy-en"><b>WARNING CONTENTS HARMFUL</b><br>Do not swallow.<br>Do not get in eyes or on skin or clothing.<br>Keep out of reach of children and pets.<br><b>IN GREDIENTS:</b> Propylene Glycol, Vegetable Glycerin, Food Grade Alcohol, Natural and Artificial Flavours.<span class="gap"></span><b>If swallowed consult poison control centre or a doctor immediately.<br>May contain nuts.</b></div>
    <div class="record"><span>BATCH :</span><span>EXPIRES :</span></div>
    <div class="rule"></div>
    <svg class="badge" viewBox="0 0 48 48" aria-label="Nicotine strength 12">
      <defs><path id="arc-12" d="M7 24 A17 17 0 0 1 41 24"/></defs>
      <circle class="ring" cx="24" cy="24" r="23"/>
      <text class="ring-text"><textPath href="#arc-12" startOffset="50%" text-anchor="middle">NICOTINE LEVEL</textPath></text>
      <circle class="dot" cx="24" cy="26" r="13"/>
      <text class="value" x="24" y="31.5" text-anchor="middle">12</text>
    </svg>
    <div class="foot"><div class="fr">Produit et emballé exclusivement pour:<br>4471920 Northfield Inc, Ashby ON, K0A 1B0</div><div class="size">30 ml<br>E-LIQUID</div><div class="en">Produced and Packaged exclusively for :<br>4471920 Northfield Inc, Ashby ON, K0A 1B0</div></div>
  </div>
  <div class="strip bottom">DANGER POISON &nbsp;DANGER POISON &nbsp;DANGER POISON &nbsp;DANGER POISON &nbsp;DANGER POISON</div>
</section>

<!-- 18 mg -->
<section class="label mg18" style="top:503px">
  <div class="strip top">18 mg/ml NICOTINE &nbsp; 18 mg/ml NICOTINE &nbsp; 18 mg/ml NICOTINE &nbsp; 18 mg/ml NICOTINE</div>
  <div class="panel">
    <svg class="swirl" viewBox="0 0 600 198" aria-hidden="true"><path d="M0 40 C120 10 200 90 320 40 S520 20 600 60" fill="none" stroke="rgba(37,42,110,.3)"/><path d="M0 60 C140 30 220 110 340 60 S540 40 600 90" fill="none" stroke="rgba(255,255,255,.12)"/></svg>
    <svg class="hazard" viewBox="0 0 26 22" aria-hidden="true"><path d="M13 1 L25 21 H1 Z" fill="var(--hazard)" stroke="#000" stroke-width="1.2"/><circle cx="13" cy="12" r="3.2" fill="#000"/><path d="M8 17 L18 14 M8 14 L18 17" stroke="#000" stroke-width="1.3"/></svg>
    <div class="watermark">50/50<br>50/50<br>50/50</div>
    <div class="brand">Velora</div>
    <div class="flavour">SWEET TOBACCO</div>
    <div class="copy-fr"><b>CONTENIR NOCIF</b><br>Ne pas avaler.<br>Ne pas mettre dans les yeux ou sur la peau ou les vêtements.<br>Tenir hors de portée des enfants et des animaux.<br><b>INGRÉDIENTS:</b> Propylène Glycol, Glycérine, Alcool de Qualité Alimentaire, Arômes Naturel et Artificiels.<span class="gap"></span><b>En cas d'ingestion consulter centre antipoison ou un médecin immédiatement. Peux contenir de noix.</b></div>
    <div class="copy-en"><b>WARNING CONTENTS HARMFUL</b><br>Do not swallow.<br>Do not get in eyes or on skin or clothing.<br>Keep out of reach of children and pets.<br><b>IN GREDIENTS:</b> Propylene Glycol, Vegetable Glycerin, Food Grade Alcohol, Natural and Artificial Flavours.<span class="gap"></span><b>If swallowed consult poison control centre or a doctor immediately.<br>May contain nuts.</b></div>
    <div class="record"><span>BATCH :</span><span>EXPIRES :</span></div>
    <div class="rule"></div>
    <svg class="badge" viewBox="0 0 48 48" aria-label="Nicotine strength 18">
      <defs><path id="arc-18" d="M7 24 A17 17 0 0 1 41 24"/></defs>
      <circle class="ring" cx="24" cy="24" r="23"/>
      <text class="ring-text"><textPath href="#arc-18" startOffset="50%" text-anchor="middle">NICOTINE LEVEL</textPath></text>
      <circle class="dot" cx="24" cy="26" r="13"/>
      <text class="value" x="24" y="31.5" text-anchor="middle">18</text>
    </svg>
    <div class="foot"><div class="fr">Produit et emballé exclusivement pour:<br>4471920 Northfield Inc, Ashby ON, K0A 1B0</div><div class="size">30 ml<br>E-LIQUID</div><div class="en">Produced and Packaged exclusively for :<br>4471920 Northfield Inc, Ashby ON, K0A 1B0</div></div>
  </div>
  <div class="strip bottom">DANGER POISON &nbsp;DANGER POISON &nbsp;DANGER POISON &nbsp;DANGER POISON &nbsp;DANGER POISON</div>
</section>

<!-- 24 mg -->
<section class="label mg24" style="top:752px">
  <div class="strip top">24 mg/ml NICOTINE &nbsp; 24 mg/ml NICOTINE &nbsp; 24 mg/ml NICOTINE &nbsp; 24 mg/ml NICOTINE</div>
  <div class="panel">
    <svg class="swirl" viewBox="0 0 600 198" aria-hidden="true"><path d="M0 40 C120 10 200 90 320 40 S520 20 600 60" fill="none" stroke="rgba(232,32,42,.3)"/><path d="M0 60 C140 30 220 110 340 60 S540 40 600 90" fill="none" stroke="rgba(255,255,255,.12)"/></svg>
    <svg class="hazard" viewBox="0 0 26 22" aria-hidden="true"><path d="M13 1 L25 21 H1 Z" fill="var(--hazard)" stroke="#000" stroke-width="1.2"/><circle cx="13" cy="12" r="3.2" fill="#000"/><path d="M8 17 L18 14 M8 14 L18 17" stroke="#000" stroke-width="1.3"/></svg>
    <div class="watermark">50/50<br>50/50<br>50/50</div>
    <div class="brand">Velora</div>
    <div class="flavour">SWEET TOBACCO</div>
    <div class="copy-fr"><b>CONTENIR NOCIF</b><br>Ne pas avaler.<br>Ne pas mettre dans les yeux ou sur la peau ou les vêtements.<br>Tenir hors de portée des enfants et des animaux.<br><b>INGRÉDIENTS:</b> Propylène Glycol, Glycérine, Alcool de Qualité Alimentaire, Arômes Naturel et Artificiels.<span class="gap"></span><b>En cas d'ingestion consulter centre antipoison ou un médecin immédiatement. Peux contenir de noix.</b></div>
    <div class="copy-en"><b>WARNING CONTENTS HARMFUL</b><br>Do not swallow.<br>Do not get in eyes or on skin or clothing.<br>Keep out of reach of children and pets.<br><b>IN GREDIENTS:</b> Propylene Glycol, Vegetable Glycerin, Food Grade Alcohol, Natural and Artificial Flavours.<span class="gap"></span><b>If swallowed consult poison control centre or a doctor immediately.<br>May contain nuts.</b></div>
    <div class="record"><span>BATCH :</span><span>EXPIRES :</span></div>
    <div class="rule"></div>
    <svg class="badge" viewBox="0 0 48 48" aria-label="Nicotine strength 24">
      <defs><path id="arc-24" d="M7 24 A17 17 0 0 1 41 24"/></defs>
      <circle class="ring" cx="24" cy="24" r="23"/>
      <text class="ring-text"><textPath href="#arc-24" startOffset="50%" text-anchor="middle">NICOTINE LEVEL</textPath></text>
      <circle class="dot" cx="24" cy="26" r="13"/>
      <text class="value" x="24" y="31.5" text-anchor="middle">24</text>
    </svg>
    <div class="foot"><div class="fr">Produit et emballé exclusivement pour:<br>4471920 Northfield Inc, Ashby ON, K0A 1B0</div><div class="size">30 ml<br>E-LIQUID</div><div class="en">Produced and Packaged exclusively for :<br>4471920 Northfield Inc, Ashby ON, K0A 1B0</div></div>
  </div>
  <div class="strip bottom">DANGER POISON &nbsp;DANGER POISON &nbsp;DANGER POISON &nbsp;DANGER POISON &nbsp;DANGER POISON</div>
</section>

</body>
</html>
```